Business card for someone who trains leaders
Organizational Development Consultant Business Card - Consulting
Organizational Development Consultant Business Card
Bright & Fun-filled
Darla Quinby
Capacity Development Adviser
(NO ADDRESS IS LISTED ON CARD)
darla@vrmthrivewell.com
www.netprofile/in/marlowquinby
I want a business card that says professional but not too corporate. I want it to only use the colors on my logo (plus white of course). I like the look of cards that have some black backgrounds, but I'm open to a lot of different looks - as long as it meshes well with the look and feel of the business card. I don't want anything too busy, but yet want something that stands out a bit.
Where Will Your Growth Lead? Let VRM Thrivewell help you find growth through organizational development, leadership coaching, and much more!
marlowquinby marlowquinby
Please don't submit generic samples with someone else's information. I'm only interested in seeing completed business cards with the information I included in the creative brief.
I would like to see some designs that are on a white background as well as a black background. I'm not sold either way, but want to see a variety. Also, on the creative brief, I left off the website. In addition to my netprofile profile, I also want the website www.vrmthrivewell.com.

```html
<!DOCTYPE html>
<html lang="en">
<head>
<meta charset="utf-8">
<title>VRM Thrivewell – Business Card</title>
<link rel="stylesheet" href="https://fonts.googleapis.com/css2?family=Open+Sans:wght@400;600;700&family=Raleway:wght@400;600&display=swap">
<style>
  :root {
    --purple: #6b2fae;
    --purple-deep: #55209a;
    --purple-light: #8446c6;
    --blue: #1f6fd1;
    --white: #ffffff;
    --ink: #3d2a55;
    --backdrop: #e9e7ec;
  }
  * { box-sizing: border-box; margin: 0; padding: 0; }
  html, body { width: 1200px; height: 908px; overflow: hidden; }
  body {
    background: var(--backdrop);
    font-family: "Open Sans", Arial, sans-serif;
    display: flex;
    align-items: center;
    justify-content: center;
    gap: 40px;
  }
  .card {
    position: relative;
    width: 560px;
    height: 320px;
    border-radius: 18px;
    overflow: hidden;
    box-shadow: 0 10px 30px rgba(40, 20, 70, 0.18);
  }

  /* Front */
  .card--front {
    background: linear-gradient(135deg, var(--purple-light) 0%, var(--purple) 45%, var(--purple-deep) 100%);
    color: var(--white);
  }
  .front__mark {
    position: absolute;
    right: -40px;
    top: 10px;
    width: 300px;
    height: 300px;
    border-radius: 50%;
    background: rgba(255, 255, 255, 0.12);
  }
  .front__content {
    position: absolute;
    left: 44px;
    top: 108px;
    width: 330px;
  }
  .brand-name {
    font-family: "Raleway", sans-serif;
    font-weight: 600;
    font-size: 30px;
    letter-spacing: 0.5px;
    line-height: 1;
  }
  .tagline {
    margin-top: 8px;
    padding-top: 6px;
    border-top: 1px solid rgba(255, 255, 255, 0.8);
    font-size: 13px;
    font-weight: 600;
    letter-spacing: 0.3px;
  }
  .front__blurb {
    margin-top: 12px;
    font-size: 12.5px;
    line-height: 1.45;
  }

  /* Back */
  .card--back { background: var(--white); }
  .back__band {
    position: absolute;
    left: 0; top: 0;
    width: 100%;
    height: 148px;
    background: linear-gradient(135deg, var(--purple-light), var(--purple-deep));
    color: var(--white);
    padding: 22px 0 0 250px;
  }
  .back__rule {
    position: absolute;
    left: 0; top: 148px;
    width: 100%;
    height: 5px;
    background: var(--blue);
    border-top: 2px solid var(--white);
  }
  .person-name { font-size: 18px; font-weight: 700; line-height: 1.1; }
  .person-title { font-size: 11.5px; margin-top: 2px; }
  .contact-list { list-style: none; margin-top: 14px; }
  .contact-list li {
    display: flex;
    align-items: center;
    gap: 8px;
    font-size: 11px;
    line-height: 1.7;
  }
  .contact-list svg { width: 11px; height: 11px; flex: none; }
  .back__logo {
    position: absolute;
    left: 0; right: 0;
    top: 190px;
    display: flex;
    flex-direction: column;
    align-items: center;
  }
  .logo-lockup { display: flex; align-items: center; gap: 12px; }
  .logo-dot {
    width: 40px; height: 40px;
    border-radius: 50%;
    background: var(--purple);
  }
  .logo-lockup .brand-name { color: var(--purple); font-size: 30px; }
  .back__logo .tagline {
    color: var(--blue);
    border-top-color: var(--blue);
    font-size: 12px;
    margin-top: 6px;
    padding-top: 4px;
  }
</style>
</head>
<body>

  <section class="card card--front" aria-label="Card front">
    <div class="front__mark" aria-hidden="true"></div>
    <div class="front__content">
      <div class="brand-name">VRM Thrivewell</div>
      <div class="tagline">Where Will Your Growth Lead?</div>
      <p class="front__blurb">Let VRM Thrivewell help you find growth through organizational development, leadership coaching, and much more!</p>
    </div>
  </section>

  <section class="card card--back" aria-label="Card back">
    <div class="back__band">
      <div class="person-name">Darla Quinby</div>
      <div class="person-title">Capacity Development Adviser</div>
      <ul class="contact-list">
        <li>
          <svg viewBox="0 0 12 12" aria-hidden="true"><path d="M3 1 L5 3.5 L4 5 C4.6 6.4 5.6 7.4 7 8 L8.5 7 L11 9 L10 11 C5.5 11 1 6.5 1 2 Z" fill="#fff"/></svg>
          555-014-2286
        </li>
        <li>
          <svg viewBox="0 0 12 12" aria-hidden="true"><rect x="1" y="2.5" width="10" height="7" fill="none" stroke="#fff" stroke-width="1.2"/><path d="M1 3 L6 7 L11 3" fill="none" stroke="#fff" stroke-width="1.2"/></svg>
          darla@vrmthrivewell.com
        </li>
        <li>
          <svg viewBox="0 0 12 12" aria-hidden="true"><rect x="1" y="1" width="10" height="10" rx="2" fill="#fff"/></svg>
          www.netprofile/in/marlowquinby
        </li>
        <li>
          <svg viewBox="0 0 12 12" aria-hidden="true"><circle cx="6" cy="6" r="5" fill="none" stroke="#fff" stroke-width="1.2"/><path d="M1 6 H11 M6 1 C3.5 4 3.5 8 6 11 M6 1 C8.5 4 8.5 8 6 11" fill="none" stroke="#fff" stroke-width="1"/></svg>
          www.vrmthrivewell.com
        </li>
      </ul>
    </div>
    <div class="back__rule" aria-hidden="true"></div>
    <div class="back__logo">
      <div class="logo-lockup">
        <span class="logo-dot" aria-hidden="true"></span>
        <span class="brand-name">VRM Thrivewell</span>
      </div>
      <div class="tagline">Where Will Your Growth Lead?</div>
    </div>
  </section>

</body>
</html>
```